Need posters that inspire entrepreneurs

I want to create beautiful, inspiring wall art. I'm looking for a designer to create an awesome sample (note this sample is not for real use). The winning design will form the foundation of our art "style" so there will be LOTS of ongoing work for the winning designer.

It's your challenge to create a style that is clean, inspiring and timeless, and possibly can be adapted to different colour palettes.

Looking for a perfect execution of words, image and design.

The attached example shows one idea. It should serve as an idea only.

Format of the images should be either rectangular or square. Exact size is preferably UK A4 (US letter) or max A3. Assume that a display would consist of a 4 x 4 image grid so size needs to allow for that in a small to medium size office.

The quotes I want in the 3 samples (each in an individual poster - not combined in 1 poster). Each quote should have it's own, the reason for three is to prove the design work on more than one quote. The quotes are:

1) Failure is the condiment that gives success its flavor.
– Dorian Welsby

2) Whether you think you can or think you can’t, you’re right.
– Oswald Pike

3) Ever tried. Ever failed. No matter. Try Again. Fail again. Fail better.
– Lionel Marwick

Each design should include the image of the person and the quote + any design elements you consider relevant. You should find relevant images of the individuals being quoted. The final images will not be published or used commercially in any way.

Font styles to use
Serif
Sans Serif

Colors

Designer to choose colors to be used in the design.

Requirements
Must have
• Words and headshot image - 1 per poster design.
• Please consider in the design that there will not always be photographs of the person quoted and as such the design will need to hold, whether the source is a photo, sketch or something else.
Nice to have
• None, but note that the final image will be printed on a wall mounted board, printed to the edge but not on the edge. The board will have black or white edges so consider in the design.
Should not have
• None

```html
<!DOCTYPE html>
<html lang="en">
<head>
<meta charset="utf-8">
<title>Failure Is the Condiment — Poster</title>
<link rel="stylesheet" href="https://fonts.googleapis.com/css2?family=Bodoni+Moda:opsz,wght@6..96,500;6..96,600&display=swap">
<style>
  :root {
    --ink: #050505;
    --green: #1fe56a;
    --photo-deep: #0b4f24;
    --photo-mid: #1f9e4b;
    --photo-light: #3fd476;
    --white: #ffffff;
    --quote-grey: #5c5c5c;
  }
  * { margin: 0; padding: 0; box-sizing: border-box; }
  html, body { width: 1200px; height: 848px; overflow: hidden; background: var(--ink); }
  .poster {
    position: relative;
    width: 1200px;
    height: 848px;
    background: var(--ink);
    overflow: hidden;
    font-family: "Bodoni Moda", "Didot", serif;
  }
  .poster__art { position: absolute; inset: 0; }
  .band { fill: var(--green); }
  .stripe { fill: var(--ink); }
  .tone-mid { stop-color: var(--photo-mid); }
  .tone-deep { stop-color: var(--photo-deep); }
  .tone-light { stop-color: var(--photo-light); }
  .fade-start { stop-color: var(--green); stop-opacity: 0; }
  .fade-end { stop-color: var(--green); stop-opacity: 1; }
  .quote-mark {
    position: absolute;
    font-family: "Bodoni Moda", "Didot", serif;
    font-weight: 600;
    color: var(--quote-grey);
    opacity: 0.75;
    font-size: 330px;
    line-height: 1;
  }
  .quote-mark--open { left: 72px; top: 522px; }
  .quote-mark--close { left: 1078px; top: 690px; }
  .quote {
    position: absolute;
    left: 262px;
    top: 612px;
    color: var(--white);
    font-size: 55px;
    font-weight: 500;
    line-height: 78px;
    letter-spacing: 0.2px;
  }
  .quote__accent { color: var(--green); }
  .attribution {
    position: absolute;
    right: 138px;
    top: 770px;
    color: var(--white);
    font-size: 22px;
    font-weight: 500;
  }
</style>
</head>
<body>
  <main class="poster">
    <svg class="poster__art" width="1200" height="848" viewBox="0 0 1200 848">
      <defs>
        <clipPath id="band-clip">
          <polygon points="0,0 1183,0 0,684"/>
        </clipPath>
        <linearGradient id="portrait-tone" x1="0" y1="0" x2="1" y2="1">
          <stop offset="0" class="tone-mid"/>
          <stop offset="0.55" class="tone-deep"/>
          <stop offset="1" class="tone-light"/>
        </linearGradient>
        <linearGradient id="portrait-fade" x1="0" y1="0" x2="1" y2="0">
          <stop offset="0" class="fade-start"/>
          <stop offset="1" class="fade-end"/>
        </linearGradient>
      </defs>
      <polygon class="band" points="0,0 1183,0 0,684"/>
      <g clip-path="url(#band-clip)">
        <g class="portrait" role="img" aria-label="Green-toned headshot of Dorian Welsby wearing a flat cap">
          <rect x="0" y="0" width="620" height="684" fill="url(#portrait-tone)"/>
          <rect x="400" y="0" width="221" height="684" fill="url(#portrait-fade)"/>
        </g>
      </g>
      <polygon class="stripe stripe--upper" points="520,0 548,0 0,317 0,301"/>
      <polygon class="stripe stripe--lower" points="585,0 650,0 0,376 0,338"/>
    </svg>

    <span class="quote-mark quote-mark--open" aria-hidden="true">&ldquo;</span>
    <span class="quote-mark quote-mark--close" aria-hidden="true">&rdquo;</span>

    <blockquote class="quote">
      <span class="quote__accent">Failure</span> is the condiment<br>
      that gives <span class="quote__accent">success</span> its flavor.
    </blockquote>
    <p class="attribution">-Dorian Welsby</p>
  </main>
</body>
</html>
```